Is your Will up to date?

We need a flyer that invites people to ask themselves if their Will is up to date.
In addition it is a known fact that people do not adjust their Will as often as they should to reflect their current wishes and circumstances.
Also, a large number of people end up having their estate pay taxes
that could be avoided if correct planning is in place.
We are offering a free of charge service the carry out a check to make sure families have in place a Will that suits their needs and circumstances and that has taken into account the tax positions and impact fully with a view to having the estate as tax efficient as possible.
A Will service is also part of the family check up.

Below is the suggested text for the flyer

A Will is one of the most important documents that we should all have. Many people are aware that if they die without having made a Will, then intestate rules apply which means in simple terms, that family assets and cash could end up in the hands of the Treasury.

While many people have looked at and acted upon creating a Will, it is fair to say that for many, the terms and wishes of the Will are often outdated. It is easy to assume that amending a Will frequently is a complicated process which it need not be.

An individual or a family Will is most important in order to ensure that upon death, your estate is dealt with and distributed in accordance with your wishes. This is also to ensure that any family are looked after by those provisions. Not only may family changes and additions affect a family Will, but there are also life changing situations that can have an effect.

Additionally, consideration needs to be given regularly to the current tax position, with specific regard to Inheritance Tax and how estate values can be legitimately reduced resulting in less tax to pay.

At Hartwell & Company we have the advantage of our Chartered Accountancy practice background, as well as also being Independent Financial Advisers. We are therefore well placed to advise families on the creation or updating of their Will, and to give advice on how to minimise tax payments.

Even for individuals and families that have had no significant changes in circumstances for many years, very often the beneficiaries may need to be updated, and even the appointment of Executors and Trustees needs to be addressed because very often, these instructions are considerably out of date.

A Will and all of its complex implications should be reviewed every one or two years and it is an extremely simple process to do this with our assistance.

So far as minimising payments for tax there are a wide range of effective methods that help do this. As general examples, there can be gifts made to family or a partner, gifts to friends, charitable donations, the use of insurance products to help settle tax liability as well as looking at placing assets into Trust. We have a wealth of experience in setting up the different types of Trust that exist and can help you easily understand how they would work for you.

When looking at the preparation of a Will, there are hundreds of questions that could be considered appropriate. However, with our experience and knowledge, and bespoke software this process can be covered within an initial meeting of less than one hour. You will have the re-assurance of knowing that every aspect has been carefully considered in preparing a Will to your circumstances and wishes.

The initial meeting and any follow up meetings are completely free of all cost and charges, and can be held at either our offices, or at your home if preferred.

We can just as easily deal with the process over the telephone if more convenient. Thereafter, we will prepare a draft Will for you, and give you confirmation as to the charges. In most cases, an individual or family Will would not normally involve charges in excess of £100.

So far as mitigating possible Inheritance Tax liabilities on the estate, we also offer the benefit of an asset and investment review at no cost. The individual or family assets are carefully considered, along with your requirements of income and growth and any specific requests or wishes that you wish to build into any trust or other methods of your choosing.

At the initial meeting or conference call we discuss all of these implications and will prepare a report and recommendations for your consideration, again free of charge. If you decide to act upon any of the recommendations, then any fees can be discussed and agreed at that stage.

All in all, whether you require assistance in preparing or updating a Will, or receiving independent advice regarding your estate assets or investments, these functions are carried out by us at no initial costs or charges.

At every step of the way there are never hidden charges or fees that you will be asked to be paid. We have over 30 years of experience in these market places, and value the service we give our clients and the reputation we gain from it.

We consider the review of a Will should be carried out at a minimum of every two years and it is a very small financial budget to allow for, against having the satisfaction of knowing these important matters are reflecting your current views, circumstances and wishes.

The same can be said for any trust and investment matters and any estate advice given. We are extremely proud and confident of the service we provide, and if any of our clients decide they do not wish to act upon the advice given, then they at least have had the benefit of a thorough review together with a recommendation without obligations of any sort.

To discuss these matters further or to make arrangements for a meeting please call our offices or email to derek@hartwellco-mail.co.uk

Content will be uploaded with next 24 hours

I am updating the brief with the wording.
It needs to be spread over the front and back of the flyer in an easy to read non boring design

Our firm logo will be updated shorty plus our Institute logo
Please make the flyer as catchy and interesting as possible.
Its a relatively boring topic for most people so it has to be eye catching rather than reading a page in a book

We will increase the budget if we are presented with a design we really like

Please note slightly amended text uploaded today

Target Market(s)

middle to upper class residents

Industry/Entity Type

Investment

Requirements
Must have
• Web address
Easy to read and understand
To look and feel catchy and not like reading a book
Some catchy graphics about tax, money, families etc

Fields where I can easily insert text and other details

```html
<!DOCTYPE html>
<html lang="en">
<head>
<meta charset="utf-8">
<title>Is Your Will Up To Date? – Hartwell &amp; Company</title>
<link rel="stylesheet" href="https://fonts.googleapis.com/css2?family=Ubuntu:wght@700&family=Arimo:ital,wght@0,400;0,700;1,700&display=swap">
<style>
  :root {
    --brand-blue: #0aaeea;
    --brand-blue-soft: #26a9e0;
    --panel-dark: #2e2e2e;
    --ink: #111111;
    --paper: #ffffff;
    --card-white: rgba(255, 255, 255, 0.82);
  }
  * { margin: 0; padding: 0; box-sizing: border-box; }
  html, body { width: 900px; height: 1200px; overflow: hidden; background: var(--paper); }
  .flyer { position: relative; width: 900px; height: 1200px; font-family: "Arimo", Arial, sans-serif; }

  .contract-photo {
    position: absolute; left: 15px; top: 760px; width: 870px; height: 425px;
    background: linear-gradient(160deg, #cfc6bc 0%, #e4ddd5 40%, #d8d0c7 70%, #b9a79a 100%);
  }
  .dark-panel {
    position: absolute; left: 15px; top: 15px; width: 870px; height: 755px;
    background: var(--panel-dark);
  }
  .dark-tab {
    position: absolute; left: 556px; top: 744px; width: 308px; height: 30px;
    background: var(--panel-dark);
    clip-path: polygon(22px 0, 286px 0, 100% 100%, 0 100%);
  }
  .gavel-photo {
    position: absolute; left: 62px; top: 15px; width: 273px; height: 780px;
    background: linear-gradient(100deg, #5a3a2c 0%, #8a6552 35%, #b89a86 65%, #d7c3b4 100%);
    clip-path: polygon(0 0, 100% 0, 100% 748px, 255px 100%, 18px 100%, 0 748px);
  }
  .top-bar {
    position: absolute; left: 15px; top: 15px; width: 870px; height: 30px;
    background: var(--brand-blue);
  }
  .web-tab {
    position: absolute; left: 528px; top: 30px; width: 342px; height: 42px;
    background: var(--brand-blue);
    clip-path: polygon(0 0, 100% 0, 100% 100%, 24px 100%);
    color: var(--paper); font-size: 20px; line-height: 42px; padding-left: 34px;
  }
  .headline {
    position: absolute; left: 362px; top: 108px; width: 480px;
    font-family: "Ubuntu", "Trebuchet MS", sans-serif; font-weight: 700;
    color: var(--brand-blue); font-size: 47px; line-height: 78px; letter-spacing: 0.5px;
  }
  .headline span { display: block; }
  .headline .line-two { text-align: right; padding-right: 8px; }
  .corner-arrow { position: absolute; left: 764px; top: 117px; }

  .method { position: absolute; left: 370px; top: 265px; width: 487px; color: var(--paper); }
  .method h2 { font-size: 16.5px; font-style: italic; font-weight: 700; margin-bottom: 8px; }
  .method p { font-size: 15.6px; line-height: 21.3px; text-align: justify; hyphens: auto; }

  .service-icon {
    position: absolute; width: 126px; height: 126px; border-radius: 50%;
    background: var(--paper); border: 11px solid var(--brand-blue);
    display: flex; align-items: center; justify-content: center;
  }
  .icon-scales { left: 374px; top: 602px; }
  .icon-gavel { left: 550px; top: 602px; }
  .icon-money { left: 735px; top: 602px; font-size: 58px; color: var(--ink); }

  .info-card { position: absolute; background: var(--card-white); }
  .info-card::after {
    content: ""; position: absolute; left: 0; right: 0; bottom: 0; height: 40px;
    background: var(--brand-blue);
  }
  .will-card { left: 62px; top: 795px; width: 271px; height: 354px; padding: 26px 16px 0 8px; }
  .will-card h3 { font-size: 20px; font-style: italic; font-weight: 700; color: var(--ink); margin-bottom: 2px; }
  .will-card p { font-size: 17.4px; line-height: 23px; color: var(--brand-blue-soft); text-align: justify; hyphens: auto; }
  .amend-card { left: 380px; top: 808px; width: 468px; height: 341px; padding: 18px 18px 0 16px; }
  .amend-card h3 { font-size: 27px; font-style: italic; font-weight: 700; color: var(--ink); margin-bottom: 14px; }
  .amend-card p { font-size: 20.6px; line-height: 27px; color: var(--brand-blue-soft); text-align: justify; }
</style>
</head>
<body>
<main class="flyer">
  <div class="contract-photo" role="img" aria-label="Photograph of a printed contract document with a red pen lying across it"></div>
  <div class="dark-panel"></div>
  <div class="dark-tab"></div>
  <div class="gavel-photo" role="img" aria-label="Close-up photograph of a wooden judge's gavel"></div>
  <div class="top-bar"></div>
  <div class="web-tab">http:// www.hartwellandco.co.uk</div>

  <h1 class="headline"><span>IS YOUR WILL</span><span class="line-two">UP TO DATE ?</span></h1>
  <svg class="corner-arrow" width="92" height="100" viewBox="0 0 92 100" aria-hidden="true">
    <polygon points="0,0 92,0 92,98 70,72 70,22" fill="#0aaeea"/>
  </svg>

  <section class="method">
    <h2>OUR METHOD OF PREPARATION OF WILL</h2>
    <p>When looking at preparation of a Will, there are hundreds of questions that could be considered appropriate. However, with our experience and knowledge, and bespoke software this process can be covered within an initial meeting of less than one hour. You will have the re-assurance of knowing that every aspect has been carefully considered in preparing a Will to your circumstances and wishes. The initial meeting and any follow up meetings are completely free of all cost and charges, and can be held at either our offices, or at your home if preferred. Thereafter, we will prepare a draft Will for you, and give you confirmation as to the charges. In most cases, an individual or family Will would typically not involve charges in excess of £100.</p>
  </section>

  <div class="service-icon icon-scales" aria-label="Scales of justice">
    <svg width="86" height="70" viewBox="0 0 86 70" aria-hidden="true">
      <g fill="#111" stroke="#111" stroke-width="2.5">
        <line x1="43" y1="6" x2="43" y2="60"/>
        <line x1="6" y1="14" x2="80" y2="10"/>
        <circle cx="43" cy="6" r="4"/>
        <line x1="10" y1="14" x2="2" y2="40" stroke-width="1.5"/>
        <line x1="10" y1="14" x2="18" y2="40" stroke-width="1.5"/>
        <line x1="76" y1="10" x2="68" y2="36" stroke-width="1.5"/>
        <line x1="76" y1="10" x2="84" y2="36" stroke-width="1.5"/>
        <path d="M0 40 H20 Q10 50 0 40Z"/>
        <path d="M66 36 H86 Q76 46 66 36Z"/>
        <path d="M30 66 Q43 56 56 66Z"/>
      </g>
    </svg>
  </div>
  <div class="service-icon icon-gavel" aria-label="Gavel">
    <svg width="90" height="70" viewBox="0 0 90 70" aria-hidden="true">
      <g fill="#111">
        <rect x="14" y="10" width="34" height="18" rx="3" transform="rotate(20 31 19)"/>
        <rect x="36" y="24" width="48" height="6" transform="rotate(20 36 27)"/>
        <rect x="6" y="52" width="42" height="7"/>
        <rect x="12" y="45" width="30" height="7"/>
      </g>
    </svg>
  </div>
  <div class="service-icon icon-money" aria-label="Money">$</div>

  <section class="info-card will-card">
    <h3>A will</h3>
    <p>A Will is one of the most important documents that we should all have. Many people are aware that if they die without a Will being in existence, then intestate rules apply which means in simple terms, that family assets and cash could end up in the hands of the Treasury.</p>
  </section>

  <section class="info-card amend-card">
    <h3>AMENDING A WILL</h3>
    <p>While many people have looked and acted upon creating a Will, it is fair to say that for the majority, the terms and wishes of the Will are often outdated. It is easy to assume that amending a Will frequently is a complicated process which it need not be.</p>
  </section>
</main>
</body>
</html>
```